KB Rubbish Removal Business Card

Hey,
I need a double sided business card designed for a rubbish removal business based in Australia. Logo is already chosen, similar colours preferred for both sides of the business card.

Details to include:

Front:

KB Rubbish Removal
Darren Holloway
Managing Director
Mobile: 0471 902 146
Email: darren@kbrubbishremoval.com.au
Website: kbrubbishremoval.com.au

Rear:

How did we do?
kbrubbishremoval.com.au/review

```html
<!DOCTYPE html>
<html lang="en">
<head>
<meta charset="utf-8">
<title>KB Rubbish Removal – Business Card</title>
<link href="https://fonts.googleapis.com/css2?family=Montserrat:wght@300;400;500;600&family=Poppins:wght@300;400&display=swap" rel="stylesheet">
<style>
  :root {
    --page-bg: #ebebeb;
    --card-bg: #ffffff;
    --pattern-tint: #f6f9f2;
    --green-bright: #28ab49;
    --green-mid: #22913f;
    --green-deep: #17692f;
    --green-ink: #1f3d1f;
    --green-rule: #1f5c2a;
    --ink: #333333;
    --white: #ffffff;
  }
  * { margin: 0; padding: 0; box-sizing: border-box; }
  html, body { width: 1200px; height: 1000px; overflow: hidden; background: var(--page-bg); }
  .canvas { position: relative; width: 1200px; height: 1000px; }

  .card { position: absolute; left: 180px; width: 842px; height: 480px; background: var(--card-bg); overflow: hidden; }
  .card--front { top: 12px; width: 841px; }
  .card--back { top: 508px; }
  .card__pattern { position: absolute; inset: 0; background: var(--pattern-tint); }

  .brand { position: absolute; left: 88px; top: 57px; display: flex; align-items: center; }
  .brand__mark { width: 86px; height: 86px; border-radius: 50%; background: var(--green-bright); }
  .brand__name {
    margin-left: 34px; font-family: "Montserrat", sans-serif; font-weight: 500;
    font-size: 38px; letter-spacing: 3.4px; color: var(--ink); white-space: nowrap;
  }

  .contact-panel {
    position: absolute; left: 53px; top: 186px; right: 0; bottom: 0;
    border-top-left-radius: 30px;
    background: radial-gradient(ellipse 70% 90% at 40% 95%, var(--green-deep) 0%, var(--green-mid) 55%, var(--green-bright) 100%);
    color: var(--white);
  }
  .person__name {
    position: absolute; left: 36px; top: 24px; font-family: "Montserrat", sans-serif;
    font-weight: 600; font-size: 31px; letter-spacing: 5.4px; white-space: nowrap;
  }
  .person__role {
    position: absolute; left: 37px; top: 62px; font-family: "Montserrat", sans-serif;
    font-weight: 300; font-size: 15px; letter-spacing: 4px; white-space: nowrap;
  }
  .person__rule { position: absolute; left: 36px; top: 107px; width: 296px; height: 3px; background: var(--white); }

  .contact {
    position: absolute; display: flex; align-items: center; gap: 12px;
    font-family: "Poppins", sans-serif; font-weight: 300; font-size: 18px; letter-spacing: 1.4px; white-space: nowrap;
  }
  .contact svg { flex: none; }
  .contact--phone { left: 39px; top: 161px; }
  .contact--web { left: 282px; top: 162px; gap: 15px; }
  .contact--email { left: 39px; top: 226px; gap: 10px; }

  .review-band {
    position: absolute; left: 0; top: 0; width: 100%; height: 110px;
    background: linear-gradient(90deg, var(--green-bright), var(--green-mid) 60%, #1e843c);
    display: flex; align-items: center; justify-content: center;
  }
  .review-band__title {
    font-family: "Montserrat", sans-serif; font-weight: 500; font-size: 39px;
    letter-spacing: 3.6px; color: var(--white); margin-top: 4px;
  }

  .steps {
    position: absolute; left: 0; right: 0; top: 150px; text-align: center;
    font-family: "Montserrat", sans-serif; font-weight: 500; font-size: 16.5px;
    letter-spacing: 1.9px; line-height: 20.5px; color: var(--green-ink);
  }
  .step__label { letter-spacing: 2.2px; }
  .step__divider { width: 94px; height: 1px; background: var(--green-mid); margin: 11px auto 15px; }
  .review-link {
    position: absolute; left: 0; right: 0; top: 446px; text-align: center;
    font-family: "Montserrat", sans-serif; font-weight: 600; font-size: 16px;
    letter-spacing: 1.6px; color: var(--green-rule);
  }
  .review-rule { position: absolute; left: 140px; width: 563px; top: 474px; height: 6px; background: var(--green-rule); }
</style>
</head>
<body>
<main class="canvas">

  <section class="card card--front" aria-label="Business card front">
    <div class="card__pattern" role="img" aria-label="Faint light green diamond pattern background"></div>

    <div class="brand">
      <div class="brand__mark"></div>
      <span class="brand__name">KB RUBBISH REMOVAL</span>
    </div>

    <div class="contact-panel">
      <h1 class="person__name">Darren Holloway</h1>
      <p class="person__role">Managing Director</p>
      <div class="person__rule"></div>

      <p class="contact contact--phone">
        <svg width="26" height="26" viewBox="0 0 24 24" aria-hidden="true">
          <path fill="#fff" d="M6.6 2.5c.6-.3 1.3 0 1.6.6l1.6 3.3c.3.6.1 1.2-.4 1.6L8 9c.9 2.3 2.7 4.3 5 5.5l1.1-1.3c.4-.5 1.1-.6 1.6-.3l3.2 1.8c.6.3.8 1 .5 1.6l-1 2c-.5 1-1.6 1.5-2.7 1.2C9.5 18 5 13 4 7.1c-.2-1.1.3-2.200 1.2-2.8z"/>
          <path fill="none" stroke="#fff" stroke-width="1.5" stroke-linecap="round" d="M14 3.5a6.5 6.5 0 0 1 6.5 6.5M14 6.8a3.3 3.3 0 0 1 3.2 3.2"/>
        </svg>
        <span>0471 902 146</span>
      </p>

      <p class="contact contact--web">
        <svg width="30" height="30" viewBox="0 0 30 30" aria-hidden="true">
          <circle cx="15" cy="15" r="14" fill="#fff"/>
          <g fill="none" stroke="var(--green-mid)" stroke-width="1.2">
            <ellipse cx="15" cy="15" rx="6" ry="13"/>
            <line x1="2" y1="15" x2="28" y2="15"/>
            <line x1="15" y1="2" x2="15" y2="28"/>
          </g>
        </svg>
        <span>kbrubbishremoval.com.au</span>
      </p>

      <p class="contact contact--email">
        <svg width="28" height="21" viewBox="0 0 28 21" aria-hidden="true">
          <rect x="0" y="0" width="28" height="21" rx="2.5" fill="#fff"/>
          <path d="M1.5 2 14 12 26.5 2" fill="none" stroke="var(--green-mid)" stroke-width="1.8"/>
        </svg>
        <span>darren@kbrubbishremoval.com.au</span>
      </p>
    </div>
  </section>

  <section class="card card--back" aria-label="Business card back">
    <div class="card__pattern" role="img" aria-label="Faint light green diamond pattern background"></div>

    <header class="review-band">
      <h2 class="review-band__title">HOW DID WE DO?</h2>
    </header>

    <div class="steps">
      <div class="step">
        <p class="step__label">STEP 1</p>
        <p>Click Book Online, select<br>from the available timeslots<br>&amp; provide some info</p>
      </div>
      <div class="step__divider"></div>
      <div class="step">
        <p class="step__label">STEP 2</p>
        <p>Receive a booking confirmation<br>email and reminder text</p>
      </div>
      <div class="step__divider" style="margin-top:19px"></div>
      <div class="step">
        <p class="step__label">STEP 3</p>
        <p>We arrive on the day to give<br>you a free written quote. If you approve,<br>we'll complete the removal!</p>
      </div>
    </div>

    <p class="review-link">kbrubbishremoval.com.au/review</p>
    <div class="review-rule"></div>
  </section>

</main>
</body>
</html>
```